Ambo postcard design

I am in charge of getting a postcard 5x7 designed for 14 artists having a gallery exhibition. We would like to use our
photo(s) with the 14 names on the front. Back of card would have gallery information.
Am sending jpeg of a past card, four images to choose from and the text for back of card.

```html
<!DOCTYPE html>
<html lang="en">
<head>
<meta charset="utf-8">
<title>Fourteen Painters – Postcard</title>
<link rel="stylesheet" href="https://fonts.googleapis.com/css2?family=Oswald:wght@300;400;500&display=swap">
<style>
  :root {
    --page-bg: #e4e4e4;
    --card-white: #ffffff;
    --ink: #1c1c1c;
    --rule: #3a3a3a;
    --band: rgba(235, 235, 235, 0.62);
    --paint-black: #0d0d12;
    --paint-yellow: #f3d21c;
    --paint-red: #e0261f;
    --paint-blue: #2f3fd0;
    --paint-cyan: #22a8e6;
    --paint-orange: #f07a1a;
  }
  html, body {
    margin: 0;
    padding: 0;
    width: 1200px;
    height: 802px;
    overflow: hidden;
    background: var(--page-bg);
  }
  .canvas {
    position: relative;
    width: 1200px;
    height: 802px;
    font-family: "Oswald", "Arial Narrow", sans-serif;
  }
  .postcard {
    position: absolute;
    top: 208px;
    width: 540px;
    height: 386px;
    box-shadow: 0 6px 18px rgba(0,0,0,0.18);
    overflow: hidden;
  }
  .postcard--back {
    left: 40px;
    background: var(--card-white);
    color: var(--ink);
  }
  .postcard--front {
    left: 620px;
    background: var(--paint-black);
  }

  /* Back side */
  .back-message {
    position: absolute;
    left: 0;
    top: 0;
    width: 262px;
    height: 100%;
    display: flex;
    flex-direction: column;
    justify-content: center;
    align-items: center;
    text-align: center;
    font-size: 9.5px;
    line-height: 1.42;
    letter-spacing: 0.02em;
    text-transform: uppercase;
    font-weight: 400;
  }
  .back-message p { margin: 0 0 9px; }
  .back-message .headline { font-size: 12px; line-height: 1.35; }
  .divider {
    position: absolute;
    left: 268px;
    top: 52px;
    width: 1px;
    height: 282px;
    background: var(--rule);
  }
  .stamp-box {
    position: absolute;
    right: 28px;
    top: 26px;
    width: 56px;
    height: 66px;
    border: 1px solid var(--rule);
  }
  .address-lines {
    position: absolute;
    left: 300px;
    top: 176px;
    width: 206px;
  }
  .address-lines span {
    display: block;
    height: 1px;
    background: var(--rule);
    margin-bottom: 29px;
  }

  /* Front side */
  .front-photo {
    position: absolute;
    inset: 0;
    background:
      radial-gradient(ellipse at 78% 30%, rgba(224,38,31,0.85), transparent 45%),
      radial-gradient(ellipse at 30% 20%, rgba(243,210,28,0.8), transparent 40%),
      radial-gradient(ellipse at 62% 62%, rgba(47,63,208,0.8), transparent 42%),
      radial-gradient(ellipse at 20% 78%, rgba(34,168,230,0.75), transparent 40%),
      radial-gradient(ellipse at 55% 88%, rgba(240,122,26,0.7), transparent 35%),
      radial-gradient(ellipse at 90% 80%, rgba(243,210,28,0.6), transparent 35%),
      var(--paint-black);
  }
  .name-band {
    position: absolute;
    left: 50px;
    top: 0;
    width: 116px;
    height: 100%;
    background: var(--band);
    text-align: center;
    color: var(--ink);
    text-transform: uppercase;
    padding-top: 40px;
    box-sizing: border-box;
  }
  .artist-list {
    list-style: none;
    margin: 0;
    padding: 0;
    font-size: 12.5px;
    line-height: 1.35;
    font-weight: 400;
  }
  .show-title {
    margin: 14px 0 14px;
    font-size: 21px;
    line-height: 1.2;
    font-weight: 500;
  }
</style>
</head>
<body>
<main class="canvas">

  <section class="postcard postcard--back" aria-label="Postcard back">
    <div class="back-message">
      <p class="headline">Gallery Lowline<br>Presents an Exhibition<br>by<br>“The Ambo Group”</p>
      <p>September 28th – October 31, 2016<br>Reception – Friday, October 2, 5–8pm</p>
      <p>Gallery Lowline<br>Lantern Row Shops, 450 Harbor Lane<br>Fairview, Virginia 22000<br>571-555-0148<br>info@gallerylowline.org<br>www.gallerylowline.org</p>
      <p>Gallery Hours: M–F 10:00am–6:00pm<br>Saturday: 10:00am–2pm<br>Parking is available in<br>metered spots on nearby streets and in public<br>garages (free on weekends and after 3pm weekdays)</p>
    </div>
    <div class="divider"></div>
    <div class="stamp-box"></div>
    <div class="address-lines"><span></span><span></span><span></span><span></span><span></span></div>
  </section>

  <section class="postcard postcard--front" aria-label="Postcard front">
    <div class="front-photo" role="img" aria-label="Photograph of bright poured paint drips in yellow, red, blue, orange and white on black, with paintbrushes lying across it"></div>
    <div class="name-band">
      <ul class="artist-list">
        <li>Ardley</li><li>Brenton</li><li>Corvell</li><li>Dunmore</li><li>Elsby</li><li>Farrand</li><li>Galway</li>
      </ul>
      <h1 class="show-title">Fourteen<br>Painters</h1>
      <ul class="artist-list">
        <li>Harlow</li><li>Iverson</li><li>Jessup</li><li>Kellen</li><li>Lorimer</li><li>Marston</li><li>Norwell</li>
      </ul>
    </div>
  </section>

</main>
</body>
</html>
```